Upmarket Artwork, Furniture Retailer needs to Improve existing Vendlo Product Template Page

We need to improve an existing design for a Vendlo product page. For professional quality we will then like to use the same designer for further work e.g vendlo store(Web page)
We need a Web Designer for an exciting new online retailer based in Sydney. Our product is upmarket Scandanavian designed indoor furniture and Rattan outdoor furniture and Modernist Artwork.
Existing Banners,Logo, text, and template can be the same but the Graphic Design need improvement to give the Vendlo product page an edge. We like the Green and Brown colours. Attached is teh logo and the extsing Product template

Reason: Thank you everyone for sending through your designs. Soem designs have come in late today and we need some extra time to contact designers. We will be in contact with you to let you know how you went. Kind Regards Melinda

Reason: Still waiting on some redesigns. My apologies for the belated reply. Thank you everyone for sending through great quality work.

Reason: My apologies for the delay. We are waiting on a re design to finalise. Thank you everyone for your patience. Cheers Melinda

Target Market(s)

Upmarket house proud 25-55 professionals

Industry/Entity Type

Graphic Design

Requirements
Must have
• To have an edge to Maximise Buyers
Nice to have
• To use the colours Greens and browns

```html
<!DOCTYPE html>
<html lang="en">
<head>
<meta charset="utf-8">
<title>Lumeno – Modern Oil Painting</title>
<link rel="stylesheet" href="https://fonts.googleapis.com/css2?family=Bodoni+Moda:wght@400&family=Roboto:wght@300;400&family=Kaushan+Script&display=swap">
<style>
  :root {
    --brown-top: #4b2d23;
    --brown-deep: #36201a;
    --brown-text: #4a2a20;
    --white: #ffffff;
    --paper: #fcfcfb;
    --green: #2f6d17;
    --ochre: #c9a24a;
    --cream: #ddd3b8;
    --slate: #8a8b80;
    --badge-light: #f4f3f1;
    --badge-mid: #dcdad6;
  }
  html, body { margin: 0; padding: 0; overflow: hidden; }
  body { width: 1200px; height: 985px; background: var(--white); position: relative; font-family: "Roboto", Arial, sans-serif; }

  .masthead {
    position: absolute; left: 0; top: 0; width: 1200px; height: 284px;
    background: linear-gradient(180deg, var(--brown-top) 0%, #432820 70%, var(--brown-deep) 100%);
  }
  .brand-name {
    position: absolute; left: 0; width: 1200px; top: 84px; text-align: center;
    font-family: "Bodoni Moda", Georgia, serif; font-weight: 400; font-size: 72px;
    color: var(--white); letter-spacing: 2px; line-height: 1;
  }
  .tagline {
    position: absolute; left: 0; width: 1200px; top: 190px; text-align: center;
    font-family: "Bodoni Moda", Georgia, serif; font-size: 34px; color: var(--white); line-height: 1;
  }
  .rule { position: absolute; top: 211px; height: 2px; background: var(--white); }
  .rule--left { left: 0; width: 348px; }
  .rule--right { left: 852px; width: 348px; }

  .main-nav {
    position: absolute; left: 0; top: 284px; width: 1200px; height: 58px; background: var(--white);
  }
  .main-nav a {
    position: absolute; top: 19px; transform: translateX(-50%); white-space: nowrap;
    font-weight: 400; font-size: 17px; color: var(--brown-text); text-decoration: none; letter-spacing: 0.2px;
  }

  .artwork {
    position: absolute; left: 0; top: 342px; width: 1200px; height: 496px;
    background: linear-gradient(160deg, var(--cream) 0%, var(--ochre) 45%, var(--slate) 100%);
    box-shadow: inset 0 8px 10px -6px rgba(0,0,0,0.45);
  }
  .artwork-pointer {
    position: absolute; left: 24px; top: 800px; width: 0; height: 0;
    border-left: 39px solid transparent; border-right: 39px solid transparent;
    border-bottom: 38px solid var(--paper);
  }

  .handmade-badge { position: absolute; left: 978px; top: 614px; width: 188px; height: 188px; }
  .handmade-badge span {
    position: absolute; font-family: "Kaushan Script", cursive; color: var(--brown-text); font-size: 44px;
    transform: rotate(-28deg);
  }

  .product-info { position: absolute; left: 0; top: 838px; width: 1200px; height: 129px; background: var(--paper); }
  .product-title {
    position: absolute; left: 56px; top: 30px; margin: 0; line-height: 1;
    font-weight: 300; font-size: 35px; color: var(--brown-text); letter-spacing: 0.3px;
  }
  .product-summary {
    position: absolute; left: 56px; top: 73px; margin: 0; line-height: 1.2;
    font-weight: 300; font-size: 21px; color: var(--brown-text);
  }
  .product-price {
    position: absolute; left: 898px; top: 38px; width: 252px; margin: 0; white-space: nowrap;
    font-family: "Bodoni Moda", Georgia, serif; font-size: 50px; color: var(--green);
    letter-spacing: 1px; line-height: 1;
    text-decoration: line-through; text-decoration-thickness: 3px;
  }
  .footer-band { position: absolute; left: 0; top: 967px; width: 1200px; height: 18px; background: var(--brown-deep); }
</style>
</head>
<body>
  <header class="masthead">
    <div class="brand-name">Lumeno</div>
    <div class="rule rule--left"></div>
    <div class="tagline">The Fine Art of Living</div>
    <div class="rule rule--right"></div>
  </header>

  <nav class="main-nav">
    <a href="#" style="left:194px">PAYMENT</a>
    <a href="#" style="left:335px">DELIVERY</a>
    <a href="#" style="left:484px">WARRANTY</a>
    <a href="#" style="left:635px">ABOUT US</a>
    <a href="#" style="left:794px">CONTACT US</a>
    <a href="#" style="left:962px">Vendlo STORE</a>
  </nav>

  <div class="artwork" role="img" aria-label="Close-up of a modern abstract oil painting with brushed metal elements"></div>
  <div class="artwork-pointer"></div>

  <div class="handmade-badge">
    <svg width="188" height="188" viewBox="0 0 188 188">
      <defs>
        <radialGradient id="badgeFill" cx="40%" cy="35%" r="70%">
          <stop offset="0%" stop-color="#f4f3f1"/>
          <stop offset="100%" stop-color="#dcdad6"/>
        </radialGradient>
      </defs>
      <circle cx="94" cy="94" r="92" fill="url(#badgeFill)"/>
      <circle cx="94" cy="94" r="84" fill="none" stroke="#7a6a62" stroke-width="1.5" stroke-dasharray="4 4"/>
    </svg>
    <span style="left:42px; top:32px">hand</span>
    <span style="left:54px; top:84px">made</span>
  </div>

  <section class="product-info">
    <h1 class="product-title">MODERN OIL PAINTING</h1>
    <p class="product-summary">Metal elements to evoke beautiful landscape, canvas-framed.</p>
    <p class="product-price">RRP $193</p>
  </section>
  <div class="footer-band"></div>
</body>
</html>
```